I need a flyer designed for a marine service company. Our company specializes in boat engine diagnostic/repair, engine service, electronic installation and repairs, bottom paint, detailing, winterization and shrink wrapping. We would like to see designs that incorporate our color scheme of deep blue, blueish gray and black (please see attached photo)

Target Market(s)

Boat owners

Industry/Entity Type

Marine

Logo Text

Kelpridge Harbor Services

Requirements
Must have
• Company logo
Nice to have
• List the services we provide.

```html
<!DOCTYPE html>
<html lang="en">
<head>
<meta charset="utf-8">
<title>Kelpridge Harbor Services – Flyer</title>
<link rel="stylesheet" href="https://fonts.googleapis.com/css2?family=Raleway:wght@400&family=Roboto+Condensed:wght@400;700&family=Roboto:wght@700&display=swap">
<style>
  :root{
    --navy:#0d4468;
    --navy-deep:#1c2f52;
    --accent:#3a9fd6;
    --mist:#d9e1ea;
    --paper:#f6f8fa;
    --rope:#e3e7ec;
    --ink:#222222;
    --white:#ffffff;
    --stage:#eceef1;
  }
  *{margin:0;padding:0;box-sizing:border-box}
  html,body{width:978px;height:1200px;overflow:hidden;background:var(--stage)}
  .flyer{
    position:absolute;left:78px;top:20px;width:730px;height:1030px;
    transform:scale(1.126);transform-origin:0 0;
    background:var(--paper);overflow:hidden;
    box-shadow:0 8px 30px rgba(0,0,0,.12);
    font-family:"Roboto Condensed",sans-serif;
  }
  .flyer__art{position:absolute;inset:0}
  .brand{
    position:absolute;left:95px;top:98px;width:260px;text-align:center;
  }
  .brand__mark{width:34px;height:34px;border-radius:50%;background:var(--navy-deep);margin:0 auto 12px}
  .brand__name{font-family:"Raleway",sans-serif;font-weight:400;font-size:21px;color:var(--navy-deep);line-height:1.2}
  .tagline{
    position:absolute;left:84px;top:249px;width:282px;height:56px;
    border-top:1px solid #8fa8c0;border-bottom:1px solid #8fa8c0;
    font-family:"Raleway",sans-serif;font-size:18px;line-height:23px;
    color:var(--ink);text-align:center;padding-top:5px;
  }
  .intro{
    position:absolute;left:84px;top:322px;width:282px;
    font-size:12.2px;line-height:17.6px;color:var(--ink);text-align:justify;
  }
  .phone{
    position:absolute;left:84px;top:460px;width:282px;text-align:center;
    font-family:"Roboto",sans-serif;font-weight:700;font-size:18px;color:var(--ink);
  }
  .services{list-style:none}
  .services__item{
    position:absolute;color:var(--white);font-weight:700;font-size:18px;line-height:23px;
    white-space:nowrap;
  }
  .contacts{list-style:none}
  .contacts__item{
    position:absolute;right:115px;font-weight:700;font-size:17px;color:var(--ink);white-space:nowrap;
  }
</style>
</head>
<body>
<main class="flyer">
  <svg class="flyer__art" width="730" height="1030" viewBox="0 0 730 1030">
    <defs>
      <linearGradient id="photoTone" x1="0" y1="0" x2="0" y2="1">
        <stop offset="0" stop-color="#6fa4d8"/>
        <stop offset="0.42" stop-color="#b9cfe0"/>
        <stop offset="0.55" stop-color="#1d2a44"/>
        <stop offset="0.7" stop-color="#566a76"/>
        <stop offset="1" stop-color="#3d4f4a"/>
      </linearGradient>
    </defs>
    <rect class="chart" width="730" height="1030" fill="#eef2f6" role="img" aria-label="Faint nautical chart in the background"/>
    <g class="chart-lines" stroke="#c9d3de" stroke-width="1">
      <line x1="90" y1="0" x2="597" y2="778"/>
      <line x1="0" y1="410" x2="597" y2="778"/>
      <line x1="597" y1="778" x2="730" y2="560"/>
      <line x1="597" y1="778" x2="730" y2="740"/>
      <line x1="597" y1="778" x2="730" y2="880"/>
      <line x1="597" y1="778" x2="690" y2="1030"/>
      <line x1="597" y1="778" x2="560" y2="1030"/>
      <line x1="597" y1="778" x2="430" y2="1030"/>
    </g>
    <!-- right service panel -->
    <path class="panel-edge" fill="var(--mist)" d="M280,0 L360,0 C405,90 445,190 475,300 C505,410 512,520 500,595 L478,605 C490,500 470,380 440,285 C405,170 345,75 280,0Z"/>
    <path class="panel" fill="var(--navy)" d="M360,0 L730,0 L730,340 C690,445 600,545 500,595 C512,520 505,410 475,300 C445,190 405,90 360,0Z"/>
    <path class="rope" fill="none" stroke="var(--rope)" stroke-width="9" d="M452,0 C475,70 500,170 512,290 C520,380 512,470 492,560"/>
    <path class="rope" fill="none" stroke="var(--rope)" stroke-width="10" d="M730,385 C680,500 600,610 520,700"/>
    <!-- lower left band -->
    <path class="band-edge" fill="var(--mist)" d="M0,575 C90,635 200,685 320,715 L320,740 C190,710 80,660 0,605Z"/>
    <path class="band" fill="var(--navy)" d="M0,600 C90,660 200,705 320,730 L470,770 L480,835 C350,880 160,892 0,878Z"/>
    <path class="rope" fill="none" stroke="var(--rope)" stroke-width="10" d="M0,902 C120,905 250,890 340,862"/>
    <path class="rope" fill="none" stroke="var(--rope)" stroke-width="9" d="M0,640 C50,670 110,700 160,718"/>
    <!-- photo frame -->
    <circle cx="339" cy="678" r="186" fill="var(--white)"/>
    <circle cx="339" cy="678" r="160" fill="url(#photoTone)" role="img" aria-label="Photo of a cabin cruiser on calm water"/>
    <!-- compass -->
    <circle cx="597" cy="778" r="62" fill="#dfe6ee" role="img" aria-label="Compass rose ornament"/>
    <!-- service markers -->
    <g class="markers" fill="var(--accent)" stroke="var(--white)" stroke-width="3">
      <circle cx="478" cy="65" r="9"/><circle cx="493" cy="120" r="9"/>
      <circle cx="505" cy="176" r="9"/><circle cx="514" cy="232" r="9"/>
      <circle cx="518" cy="289" r="9"/><circle cx="518" cy="348" r="9"/>
      <circle cx="516" cy="405" r="9"/><circle cx="508" cy="463" r="9"/>
      <circle cx="497" cy="518" r="9"/>
    </g>
    <!-- phone icon -->
    <circle cx="225" cy="428" r="19" fill="var(--accent)"/>
    <path d="M216,419 l5,-3 4,7 -3,3 c1,4 4,7 8,8 l3,-3 7,4 -3,5 c-11,1 -22,-10 -21,-21z" fill="var(--white)"/>
    <!-- contact icons -->
    <rect x="635" y="892" width="20" height="20" rx="3" fill="#3b5b9a"/>
    <rect x="635" y="924" width="20" height="20" rx="5" fill="#c13584"/>
    <g class="mail-icon" fill="none" stroke="var(--accent)" stroke-width="1.6">
      <rect x="635" y="958" width="21" height="14"/>
      <path d="M635,958 l10.5,8 10.5,-8"/>
    </g>
  </svg>

  <header class="brand">
    <div class="brand__mark"></div>
    <div class="brand__name">Kelpridge Harbor Services</div>
  </header>

  <p class="tagline">servicing all models of inboard and outboard vessels</p>

  <p class="intro">Kelpridge Harbor Services is a full mobile marine service capable of servicing all makes and models of inboard and outboard vessels. We offer dock side service, engine diagnostics, maintenance and repair, and much more.</p>

  <p class="phone">+1 555-014-2290</p>

  <ul class="services">
    <li class="services__item" style="left:497px;top:53px">Maintenance &amp; Repairs</li>
    <li class="services__item" style="left:512px;top:108px">Electrical Installs &amp; Wiring</li>
    <li class="services__item" style="left:526px;top:164px">Engine Diagnostics</li>
    <li class="services__item" style="left:535px;top:220px">Dock Side Service</li>
    <li class="services__item" style="left:541px;top:278px">Bottom Painting</li>
    <li class="services__item" style="left:540px;top:337px">Shrink Wrapping</li>
    <li class="services__item" style="left:540px;top:383px">Winterizing<br>&nbsp;&amp; Summerizing</li>
    <li class="services__item" style="left:531px;top:452px">Detailing</li>
    <li class="services__item" style="left:520px;top:507px">Teak Work</li>
  </ul>

  <ul class="contacts">
    <li class="contacts__item" style="top:891px">facebook.com/KelpridgeHarborServices/</li>
    <li class="contacts__item" style="top:923px">@KelpridgeHarborServices</li>
    <li class="contacts__item" style="top:954px">kelpridgeharbor@mailbox.example</li>
  </ul>
</main>
</body>
</html>
```